Letterhead for a German Distribution/Manufacturing Company

We need a professional Letterhead in a unique Design.
not to playful.
The Letterhead has to show show that we are a international company with headquater in Germany.
all details like adress, Vat Tax Number, Bank Accout, Eori, email, Company number has to be on the Letterhead.
for example use: VAT TAX DE5704168 Bank Account: Norrfeld Bank IBAN DE421705238ß310482 Swift: KOLV3154802 EORI 3041296587 Company Number: HRB 61508 Adress: VOLTRINA UG Amsel Strasse 7 Postal Code 04683 City Halvenbrück Country: Germany Email: info@voltrina-example.com
the design can be colored but doesnt have to be
Industry/Entity Type
Manufacturing and international distribution
Requirements
Must have
- show that we are a international company with headquater in Germany. our company infos and logo

```html
<!DOCTYPE html>
<html lang="en">
<head>
<meta charset="utf-8">
<title>VOLTRINA Letterhead</title>
<link href="https://fonts.googleapis.com/css2?family=Montserrat:wght@400;500;600&family=Roboto:wght@400;500;700&display=swap" rel="stylesheet">
<style>
  :root {
    --backdrop: #c9c9c9;
    --paper: #fbfbfa;
    --ink: #2b2b2b;
    --ink-soft: #3d3d3d;
    --rule: #3a3a3a;
    --gold: #b48f3a;
    --sign-tone: #e4e4e2;
  }
  html, body {
    margin: 0;
    padding: 0;
    width: 1073px;
    height: 1200px;
    overflow: hidden;
    background: var(--backdrop);
  }
  .letterhead {
    position: absolute;
    left: 128px;
    top: 21px;
    width: 817px;
    height: 1157px;
    background: var(--paper);
    box-shadow: 0 2px 10px rgba(0,0,0,0.12);
    font-family: "Roboto", Arial, sans-serif;
    color: var(--ink);
  }
  .brand {
    position: absolute;
    top: 80px;
    left: 0;
    width: 100%;
    display: flex;
    justify-content: center;
    align-items: center;
    gap: 14px;
  }
  .brand-dot {
    width: 34px;
    height: 34px;
    border-radius: 50%;
    background: var(--gold);
  }
  .brand-name {
    font-family: "Montserrat", Arial, sans-serif;
    font-weight: 600;
    font-size: 42px;
    letter-spacing: 1px;
    color: var(--ink);
  }
  .frame { position: absolute; left: 0; top: 0; }
  .address-block {
    position: absolute;
    left: 215px;
    top: 218px;
    font-size: 10.5px;
    line-height: 1;
  }
  .address-block p { margin: 0; position: absolute; white-space: nowrap; }
  .recipient-label { top: 0; }
  .recipient-name { top: 18px; font-weight: 700; font-size: 12px; }
  .recipient-role { top: 38px; }
  .company-name { top: 70px; font-weight: 700; font-size: 12px; }
  .company-phone { top: 90px; }
  .company-email { top: 108px; }
  .letter-date {
    position: absolute;
    margin: 0;
    right: 163px;
    top: 289px;
    font-size: 10.5px;
    line-height: 1;
  }
  .letter-body {
    position: absolute;
    left: 215px;
    top: 378px;
    width: 439px;
    font-size: 11px;
    line-height: 18.5px;
    color: var(--ink-soft);
    text-align: justify;
  }
  .letter-body p { margin: 0 0 18.5px; }
  .letter-body .emphasis { font-weight: 700; color: var(--ink); }
  .signature-mark {
    position: absolute;
    left: 215px;
    top: 880px;
    width: 115px;
    height: 32px;
    background: linear-gradient(90deg, var(--sign-tone), rgba(228,228,226,0.3));
    border-radius: 3px;
  }
  .signatory {
    position: absolute;
    left: 215px;
    top: 928px;
    font-size: 10.5px;
  }
  .signatory p { margin: 0; }
  .signatory-name { font-weight: 700; font-size: 12px; margin-bottom: 6px !important; }
  .company-details {
    position: absolute;
    left: 126px;
    top: 1008px;
    font-family: "Montserrat", Arial, sans-serif;
    font-size: 8.6px;
    color: var(--ink);
  }
  .company-details p { margin: 0; position: absolute; white-space: nowrap; }
  .detail-vat { top: 0; }
  .detail-bank { top: 12px; }
  .detail-register { top: 35px; }
  .detail-email { top: 58px; }
</style>
</head>
<body>
  <main class="letterhead">
    <header class="brand">
      <span class="brand-dot"></span>
      <span class="brand-name">VOLTRINA</span>
    </header>

    <svg class="frame" width="817" height="1157" viewBox="0 0 817 1157" aria-hidden="true">
      <line x1="59" y1="176" x2="758" y2="176" stroke="var(--rule)" stroke-width="1"/>
      <line x1="98" y1="176" x2="98" y2="1097" stroke="var(--rule)" stroke-width="1"/>
      <line x1="59" y1="1097" x2="758" y2="1097" stroke="var(--rule)" stroke-width="1"/>
      <g class="icon-pin">
        <circle cx="98" cy="1046" r="10" fill="var(--paper)" stroke="var(--rule)" stroke-width="1"/>
        <path d="M98 1052 C94 1047 93 1045 93 1043 A5 5 0 0 1 103 1043 C103 1045 102 1047 98 1052 Z" fill="var(--gold)"/>
        <circle cx="98" cy="1043" r="1.8" fill="var(--paper)"/>
      </g>
      <g class="icon-globe">
        <circle cx="98" cy="1069" r="10" fill="var(--paper)" stroke="var(--rule)" stroke-width="1"/>
        <circle cx="98" cy="1069" r="5.5" fill="none" stroke="var(--gold)" stroke-width="1.4"/>
        <ellipse cx="98" cy="1069" rx="2.3" ry="5.5" fill="none" stroke="var(--gold)" stroke-width="1"/>
        <line x1="92.5" y1="1069" x2="103.5" y2="1069" stroke="var(--gold)" stroke-width="1"/>
      </g>
    </svg>

    <section class="address-block">
      <p class="recipient-label">To</p>
      <p class="recipient-name">Martin Hale</p>
      <p class="recipient-role">Chairman and CEO</p>
      <p class="company-name">Company, Inc.</p>
      <p class="company-phone">+00 123 4567890</p>
      <p class="company-email">yourinfo@example.com</p>
    </section>

    <p class="letter-date">14 September 2025</p>

    <article class="letter-body">
      <p>Lorem ipsum dolor sit amet, consectetur adipisicing elit, sed do eiusmod tempor incididunt ut labore et dolore magna aliqua. Ut enim ad minim veniam, quis nostrud exercitation ullamco laboris nisi ut aliquip ex ea commodo consequat. Duis aute irure dolor in reprehenderit in voluptate velit esse cillum dolore eu fugiat nulla pariatur. Excepteur sint occaecat cupidatat non proident, sunt in culpa qui officia deserunt mollit anim id est laborum. Sed ut perspiciatis unde omnis iste natus error sit voluptatem accusantium doloremque laudantium, totam rem aperiam, eaque ipsa quae ab illo inventore veritatis et quasi architecto beatae vitae dicta sunt explicabo. Nemo enim ipsam voluptatem quia voluptas sit aspernatur aut odit aut fugit, sed quia consequuntur magni dolores eos qui ratione voluptatem sequi nesciunt. Neque porro quisquam est, qui dolorem ipsum quia dolor sit amet, consectetur, adipisci velit, sed quia non numquam eius modi tempora incidunt ut labore et dolore magnam aliquam quaerat voluptatem.</p>
      <p class="emphasis">Sed ut perspiciatis unde omnis rem iste natus error aperiam voluptatem accusantium doloremque laudantium, totam rem aperiam, eaque ipsa quae ab illo inventore veritatis et quasi architecto beatae vitae dicta sunt explicabo. Nemo enim ipsam voluptatem quia voluptas sit aspernatur aut odit aut fugit, sed quia consequuntur magni dolores eos qui ratione voluptatem sequi nesciunt.</p>
      <p>Neque porro quisquam est, qui dolorem ipsum quia dolor sit amet, consectetur, adipisci velit, sed quia non numquam eius modi tempora incidunt ut labore et dolore voluptatem quia voluptas magnam.</p>
    </article>

    <div class="signature-mark" role="img" aria-label="Handwritten signature of Clara Weiss"></div>

    <section class="signatory">
      <p class="signatory-name">Clara Weiss</p>
      <p class="signatory-role">Public Relations Manager</p>
    </section>

    <footer class="company-details">
      <p class="detail-vat">VAT TAX DE5704168</p>
      <p class="detail-bank">Bank Account: Norrfeld Bank IBAN DE421705238ß310482&nbsp; Swift: KOLV3154802 EORI 3041296587</p>
      <p class="detail-register">HRB 61508, VOLTRINA UG Amsel Strasse 7 Postal Code 04683 City Halvenbrück Germany</p>
      <p class="detail-email">Email: info@voltrina-example.com</p>
    </footer>
  </main>
</body>
</html>
```